Webdesign Tischlerei Wolbeck GmbH
Zielgruppe
Tischlerei - Meisterbetrieb -> Zielgruppe Privatkunden + gewerbliche Kunden
Aufgabenstellung
KEINE Kopie der alten Seite, da sich das gesamte Erscheinungsbild wesentlich moderner gestaltet... aufbauend auf dem neuen Unternehmenslogo. Es soll mit den vorhandenen Farben aus dem Logo gearbeitet werden - jedoch nicht verspielt sein.
ACHTUNG: bei den beiden mitgelieferten Dateien, welche dir Icons als Abbildung haben, ist nicht korrekte Logo verbaut, sofern diese Icons nicht verwendbar sind, bitte passende Logos für die einzelnen Kategoerien Wählen.

```html
<!DOCTYPE html>
<html lang="de">
<head>
<meta charset="utf-8">
<title>Tischlerei Wolbeck GmbH – Startseite</title>
<link rel="stylesheet" href="https://fonts.googleapis.com/css2?family=Montserrat:wght@400;500;600&display=swap">
<style>
  :root {
    --page-bg: #e5e5e5;
    --header-bg: #1c2424;
    --copper: #b07a45;
    --white: #ffffff;
    --hero-dark: #221c18;
    --hero-mid: #3b2f26;
    --hero-warm: #4a3626;
    --band: rgba(255,255,255,0.24);
  }
  * { margin: 0; padding: 0; box-sizing: border-box; }
  html, body { width: 1200px; height: 1200px; overflow: hidden; background: var(--page-bg); }
  body { font-family: "Montserrat", sans-serif; color: var(--white); }

  .site {
    position: absolute; left: 42px; top: 262px;
    width: 1116px; height: 622px; overflow: hidden;
  }

  /* Header */
  .site-header {
    position: absolute; left: 0; top: 0; width: 100%; height: 88px;
    background: var(--header-bg);
  }
  .brand-name {
    position: absolute; left: 53px; top: 36px;
    font-size: 16px; font-weight: 500; letter-spacing: 0.02em;
    color: var(--white); white-space: nowrap;
  }

  .main-nav a {
    position: absolute; top: 35px;
    font-size: 11px; font-weight: 500; letter-spacing: 0.22em;
    color: var(--white); text-decoration: none; white-space: nowrap;
  }
  .main-nav a.is-active::after {
    content: ""; position: absolute; left: 0; top: 16px; width: 22px; height: 1.5px; background: var(--copper);
  }

  .header-contact { position: absolute; left: 909px; top: 58px; font-size: 7px; line-height: 12.5px; letter-spacing: 0.01em; }
  .header-contact div { display: flex; align-items: center; gap: 4px; white-space: nowrap; }
  .header-contact svg { width: 7px; height: 7px; fill: var(--white); }

  .menu-toggle { position: absolute; left: 1069px; top: 31px; width: 21px; height: 20px; }
  .menu-toggle span { position: absolute; left: 0; width: 21px; height: 1.5px; background: var(--copper); }
  .menu-toggle span:nth-child(1) { top: 0; }
  .menu-toggle span:nth-child(2) { top: 9px; }
  .menu-toggle span:nth-child(3) { top: 18px; }

  /* Hero */
  .hero { position: absolute; left: 0; top: 88px; width: 100%; height: 534px; }
  .hero-image {
    position: absolute; inset: 0;
    background:
      linear-gradient(90deg, rgba(60,45,34,0.9) 0%, rgba(40,32,27,0.2) 30%, rgba(34,28,24,0) 50%, rgba(60,42,30,0.5) 75%, rgba(30,25,22,0.6) 100%),
      linear-gradient(180deg, var(--hero-mid) 0%, var(--hero-dark) 55%, var(--hero-warm) 100%);
  }
  .hero-line {
    position: absolute; left: 0; right: 0; text-align: center;
    font-weight: 400; font-size: 36px; line-height: 1; letter-spacing: 0.31em; white-space: nowrap;
    padding-left: 0.31em;
  }
  .hero-line--one { top: 123px; }
  .hero-band { position: absolute; left: 272px; top: 167px; width: 560px; height: 60px; background: var(--band); }
  .hero-line--two { top: 179px; }
  .hero-line--three { top: 234px; color: var(--copper); }

  .hero-intro {
    position: absolute; left: 0; right: 0; top: 299px; text-align: center;
    font-size: 13.5px; line-height: 20px; letter-spacing: 0.12em;
  }
  .hero-button {
    position: absolute; left: 468px; top: 371px; width: 190px; height: 45px;
    background: var(--white); color: #1c1c1c; text-decoration: none;
    display: flex; align-items: center; justify-content: center;
    font-size: 12.5px; font-weight: 500; letter-spacing: 0.24em;
  }
</style>
</head>
<body>
  <div class="site">
    <header class="site-header">
      <span class="brand-name">Tischlerei Wolbeck GmbH</span>

      <nav class="main-nav">
        <a href="#" class="is-active" style="left:363px">HOME</a>
        <a href="#" style="left:440px">LEISTUNGEN</a>
        <a href="#" style="left:563px">ÜBER UNS</a>
        <a href="#" style="left:672px">REFERENZEN</a>
        <a href="#" style="left:810px">SERVICE</a>
        <a href="#" style="left:909px">KONTAKT</a>
      </nav>

      <div class="header-contact">
        <div>
          <svg viewBox="0 0 24 24"><path d="M6.6 10.8a15.1 15.1 0 0 0 6.6 6.6l2.2-2.2a1 1 0 0 1 1-.25 11.4 11.4 0 0 0 3.6.57 1 1 0 0 1 1 1V20a1 1 0 0 1-1 1A17 17 0 0 1 3 4a1 1 0 0 1 1-1h3.5a1 1 0 0 1 1 1c0 1.25.2 2.45.57 3.57a1 1 0 0 1-.25 1z"/></svg>
          <span>03741 552018</span>
        </div>
        <div>
          <svg viewBox="0 0 24 24"><path d="M2 5h20v14H2z M2 5l10 8 10-8" fill="none" stroke="#fff" stroke-width="3"/></svg>
          <span>info@tischlerei-wolbeck.de</span>
        </div>
      </div>

      <div class="menu-toggle" aria-label="Menü"><span></span><span></span><span></span></div>
    </header>

    <section class="hero">
      <div class="hero-image" role="img" aria-label="Dunkles Interieur mit Holzlamellenwand, Sideboard mit Vase und Trockenzweigen sowie einer Holztür"></div>
      <h1 class="hero-line hero-line--one">Wir gestalten Räume.</h1>
      <div class="hero-band"></div>
      <p class="hero-line hero-line--two">Mit Holz. Mit Herz.</p>
      <p class="hero-line hero-line--three">Mit Handwerk.</p>
      <p class="hero-intro">Willkommen bei der Tischlerei Wolbeck — Ihrer Tischlerei für individuelle<br>Lösungen aus Holz, Glas und modernen Werkstoffen.</p>
      <a href="#" class="hero-button">Mehr erfahren.</a>
    </section>
  </div>
</body>
</html>
```